Need wine label for brand that is named: Casmerel Vineyards & Winery

Casmerel is a yoga way of breathing. In Sanskrit Casmerel means "flying up." I would like a creative wine label that articulates Casmerel. The label should include a graphic and the name Casmerel on one line and Vineyards & Winery in smaller print underneath Casmerel.

```html
<!DOCTYPE html>
<html lang="en">
<head>
<meta charset="utf-8">
<title>Casmerel Vineyards &amp; Winery – Wine Label</title>
<link rel="stylesheet" href="https://fonts.googleapis.com/css2?family=Josefin+Sans:wght@400;600&family=Oswald:wght@400&display=swap">
<style>
  :root {
    --teal: #0fa59a;
    --teal-soft: rgba(15,165,154,0.18);
    --navy: #154a62;
    --leaf: #8dc63f;
    --paper: #ffffff;
    --backdrop: #f1ece6;
  }
  * { box-sizing: border-box; margin: 0; padding: 0; }
  html, body {
    width: 1200px;
    height: 1200px;
    overflow: hidden;
    background: var(--backdrop);
  }
  .label {
    position: absolute;
    left: 220px;
    top: 30px;
    width: 760px;
    height: 1140px;
    background: var(--paper);
    box-shadow: 0 4px 18px rgba(0,0,0,0.12);
    overflow: hidden;
  }
  .arch-frame {
    position: absolute;
    left: 19px;
    top: 23px;
    width: 720px;
    height: 552px;
    border: 2px solid var(--leaf);
    border-bottom: none;
    border-radius: 126px 126px 0 0;
  }
  .brand-mark {
    position: absolute;
    left: 305px;
    top: 95px;
    width: 150px;
    height: 150px;
    border-radius: 50%;
    background: var(--teal-soft);
  }
  .brand-name {
    position: absolute;
    left: 0;
    width: 100%;
    top: 300px;
    text-align: center;
    font-family: "Josefin Sans", sans-serif;
    font-weight: 600;
    font-size: 112px;
    line-height: 1;
    color: var(--teal);
    letter-spacing: 2px;
  }
  .flourish {
    position: absolute;
    left: 127px;
    top: 490px;
    width: 505px;
    height: 38px;
    border-radius: 19px;
    background: linear-gradient(90deg, rgba(15,165,154,0) 0%, rgba(15,165,154,0.35) 50%, rgba(15,165,154,0) 100%);
  }
  .tagline {
    position: absolute;
    left: 0;
    width: 100%;
    top: 562px;
    text-align: center;
    font-family: "Josefin Sans", sans-serif;
    font-weight: 400;
    font-size: 36px;
    font-variant: small-caps;
    letter-spacing: 6px;
    color: var(--navy);
  }
  .vintage-rule {
    position: absolute;
    left: 0;
    top: 618px;
    width: 760px;
    height: 52px;
  }
  .vintage {
    position: absolute;
    left: 280px;
    top: 626px;
    width: 199px;
    height: 40px;
    background: var(--navy);
    color: var(--paper);
    font-family: "Josefin Sans", sans-serif;
    font-size: 36px;
    letter-spacing: 8px;
    text-align: center;
    line-height: 44px;
    padding-left: 8px;
  }
  .pattern-field {
    position: absolute;
    left: 0;
    top: 697px;
    width: 100%;
    height: 363px;
    background: linear-gradient(180deg, rgba(255,255,255,1) 0%, rgba(141,198,63,0.35) 45%, rgba(15,165,154,0.75) 80%, rgba(21,74,98,0.85) 100%);
  }
  .legal-band {
    position: absolute;
    left: 0;
    top: 1060px;
    width: 100%;
    height: 80px;
    background: var(--leaf);
    display: flex;
    align-items: center;
    justify-content: center;
    gap: 10px;
    font-family: "Oswald", sans-serif;
    font-size: 21px;
    color: var(--paper);
    text-transform: uppercase;
    white-space: nowrap;
  }
  .legal-band .bullet {
    width: 6px;
    height: 6px;
    background: var(--paper);
    display: inline-block;
  }
</style>
</head>
<body>
  <main class="label">
    <div class="arch-frame"></div>

    <div class="brand-mark" role="img" aria-label="Brand mark placeholder above the name"></div>

    <h1 class="brand-name">Casmerel</h1>

    <div class="flourish" role="img" aria-label="Decorative teal flourish beneath the name"></div>

    <p class="tagline">Vineyards &amp; Winery</p>

    <svg class="vintage-rule" viewBox="0 0 760 52" aria-hidden="true">
      <line x1="0" y1="27" x2="240" y2="27" stroke="#154a62" stroke-width="2"/>
      <circle cx="250" cy="27" r="4" fill="#154a62"/>
      <circle cx="509" cy="27" r="4" fill="#154a62"/>
      <line x1="519" y1="27" x2="760" y2="27" stroke="#154a62" stroke-width="2"/>
    </svg>
    <div class="vintage">2019</div>

    <div class="pattern-field" role="img" aria-label="Geometric triangle pattern in greens and teals rising from the bottom"></div>

    <footer class="legal-band">
      <span class="bullet"></span><span>Produced &amp; bottled by Vineyards Wines</span>
      <span class="bullet"></span><span>Address</span>
      <span class="bullet"></span><span>Alc. 13.0% by vol.</span>
      <span class="bullet"></span><span>750ml</span>
    </footer>
  </main>
</body>
</html>
```